Business card for Luxury Portable Restroom Trailer company

We are a Luxury Portable Restroom Trailer Company Called PELIKAR HIRES. Based in Orange County California. We provide portable restroom trailers for events, such as, Weddings, Concerts, Charity events, Sporting events, Tournaments, Corporate events, ect. We rent and Sell the Luxury restrooms. Our colors are white, grey, and Orange. As you will see in the logo we uploaded.
There are 2 people in the company so the names and titles will change for the 3 people but card will remain the same. Here is the information for each Person: Dennis Moyle CFO 555 018-3647
next Person: Wesley Tanford VP 555 018-3647
Next Person: Miles Tanford CEO 555 018-3647
Information to include on the card: Luxury Restroom Trailers Rental and Sales. Weddings, Concerts, Charity, Sporting and Corp. Events.

```html
<!DOCTYPE html>
<html lang="en">
<head>
<meta charset="utf-8">
<title>PELIKAR HIRES – Business Card</title>
<link href="https://fonts.googleapis.com/css2?family=Arimo:wght@400;700&display=swap" rel="stylesheet">
<style>
  :root {
    --page-bg: #3b3b3b;
    --card-bg: #2e2e2e;
    --brand-orange: #f26a1b;
    --text-light: #f2f2f2;
    --text-muted: #c9c9c9;
    --emboss-grey: #4a4a4a;
    --divider: #5a5a5a;
  }
  * { box-sizing: border-box; margin: 0; padding: 0; }
  html, body {
    width: 1200px; height: 689px; overflow: hidden;
    background: var(--page-bg);
    font-family: "Arimo", Arial, sans-serif;
  }
  .sheet {
    position: relative; width: 1200px; height: 689px;
  }
  .card {
    position: absolute; top: 195px;
    width: 525px; height: 300px;
    background: var(--card-bg);
    border: 2px solid var(--brand-orange);
    border-radius: 16px;
  }
  .card--front { left: 50px; }
  .card--back { left: 625px; }

  /* Front */
  .front-wordmark {
    position: absolute; top: 92px; left: 0; right: 0;
    text-align: center;
    font-weight: 700; font-size: 40px; letter-spacing: 3px;
    color: var(--emboss-grey);
  }
  .front-tagline {
    position: absolute; bottom: 48px; left: 0; right: 0;
    text-align: center; color: var(--text-light);
    font-size: 14px; line-height: 1.45;
  }

  /* Back */
  .back-wordmark {
    position: absolute; top: 160px; left: 34px;
    display: flex; align-items: center; gap: 8px;
    font-weight: 700; font-size: 24px; letter-spacing: 1.5px;
    color: var(--brand-orange);
  }
  .back-wordmark .mark {
    width: 14px; height: 14px; background: var(--brand-orange);
  }
  .divider {
    position: absolute; top: 70px; left: 282px;
    width: 1px; height: 110px; background: var(--divider);
  }
  .contact {
    position: absolute; top: 72px; left: 300px;
  }
  .contact .name {
    color: var(--brand-orange); font-weight: 700; font-size: 20px;
    text-transform: uppercase;
  }
  .contact .title {
    color: var(--text-muted); font-size: 12px; margin: 2px 0 10px;
  }
  .contact ul { list-style: none; }
  .contact li {
    display: flex; align-items: center; gap: 8px;
    color: var(--text-light); font-size: 13px; line-height: 22px;
  }
  .contact svg { width: 11px; height: 11px; fill: var(--brand-orange); flex: none; }
</style>
</head>
<body>
<main class="sheet">
  <section class="card card--front">
    <div class="front-wordmark">PELIKAR HIRES</div>
    <p class="front-tagline">
      Luxury Restroom Trailers Rental and Sales.<br>
      Weddings • Concerts • Charity • Sporting and Corp. Events
    </p>
  </section>

  <section class="card card--back">
    <div class="back-wordmark"><span class="mark"></span>PELIKAR HIRES</div>
    <div class="divider"></div>
    <div class="contact">
      <div class="name">Dennis Moyle</div>
      <div class="title">CFO</div>
      <ul>
        <li>
          <svg viewBox="0 0 24 24"><path d="M6.6 10.8a15 15 0 0 0 6.6 6.6l2.2-2.2c.3-.3.7-.4 1-.2 1.1.4 2.3.6 3.6.6.6 0 1 .4 1 1V20c0 .6-.4 1-1 1A17 17 0 0 1 3 4c0-.6.4-1 1-1h3.5c.6 0 1 .4 1 1 0 1.3.2 2.5.6 3.6.1.3 0 .7-.2 1z"/></svg>
          555 018-3647
        </li>
        <li>
          <svg viewBox="0 0 24 24"><path d="M2 5h20v14H2zm2 2v.5l8 5 8-5V7l-8 5z"/></svg>
          info@pelikarhires.com
        </li>
        <li>
          <svg viewBox="0 0 24 24"><path d="M12 2a10 10 0 1 0 0 20 10 10 0 0 0 0-20zm6.9 6h-3a15 15 0 0 0-1.3-3.9A8 8 0 0 1 18.9 8zM12 4c.8 1.2 1.5 2.5 1.9 4h-3.8c.4-1.5 1.1-2.8 1.9-4zM4.3 14a8 8 0 0 1 0-4h3.4a16 16 0 0 0 0 4zm.8 2h3c.3 1.4.8 2.7 1.3 3.9A8 8 0 0 1 5.1 16zm3-8h-3a8 8 0 0 1 4.3-3.9C8.9 5.3 8.4 6.6 8.1 8zM12 20c-.8-1.2-1.5-2.5-1.9-4h3.8c-.4 1.5-1.1 2.8-1.9 4zm2.3-6H9.7a14 14 0 0 1 0-4h4.6a14 14 0 0 1 0 4zm.3 5.9c.5-1.2 1-2.5 1.3-3.9h3a8 8 0 0 1-4.3 3.9zm1.7-5.9a16 16 0 0 0 0-4h3.4a8 8 0 0 1 0 4z"/></svg>
          www.pelikarhires.com
        </li>
      </ul>
    </div>
  </section>
</main>
</body>
</html>
```